New career and executive coaching business needs a business card design including logo

Company name: 'Harbourline Career Partners.' The aim of my coaching engagements is to help people improve their communication in the workplace and achieve their career goals. The process involves working with individuals to help them uncover their strengths and talents, then leverage those to improve their working lives. The Tellwood Inventory is the starting point to the process. I am after an exciting and interesting business card design (including logo)which is professional yet will still get people's attention.

Industry/Entity Type

Business

Contact Information for Business Card

Name: Gavin Holloway
Position: Owner
Address: 58 Pellimore Cres, Wardell Vic 3197
Phone: 0481937145
Website: harbourlinecareer.com.au
Email: gavin@hcp.com.au

Colors
33a6d7
00a990
0355a3
3176b5

Requirements
Must have
• logo

```html
<!DOCTYPE html>
<html lang="en">
<head>
<meta charset="utf-8">
<title>Harbourline Career Partners – Business Card</title>
<link rel="stylesheet" href="https://fonts.googleapis.com/css2?family=Tinos:wght@400;700&family=Arimo:wght@400&display=swap">
<style>
  :root {
    --page-bg: #eceef1;
    --card-white: #ffffff;
    --sky: #33a6d7;
    --navy: #0355a3;
    --mid-blue: #3176b5;
    --ink: #111111;
    --poly-light: #c9d8ee;
    --poly-mid: #6fb3dd;
    --poly-deep: #5d86c6;
  }
  * { box-sizing: border-box; margin: 0; padding: 0; }
  html, body { width: 1200px; height: 902px; overflow: hidden; }
  body {
    background: var(--page-bg);
    display: flex;
    flex-direction: column;
    align-items: center;
    justify-content: center;
    gap: 40px;
  }
  .card {
    position: relative;
    width: 700px;
    height: 400px;
    overflow: hidden;
    box-shadow: 0 6px 18px rgba(0,0,0,0.18);
  }

  /* Back side */
  .card-back__art {
    position: absolute; inset: 0;
    background:
      radial-gradient(circle at 30% 55%, rgba(255,255,255,0.75), transparent 30%),
      linear-gradient(135deg, var(--poly-light) 0%, var(--poly-mid) 45%, var(--sky) 70%, var(--poly-deep) 100%);
  }
  .card-back__name {
    position: absolute; left: 0; right: 0; top: 172px;
    text-align: center;
    font-family: "Tinos", serif;
    font-weight: 700;
    font-size: 46px;
    letter-spacing: 1px;
    color: var(--ink);
  }

  /* Front side */
  .card-front { background: var(--card-white); }
  .card-front__wave { position: absolute; inset: 0; }
  .card-front__company {
    position: absolute; left: 70px; top: 58px;
    font-family: "Tinos", serif;
    font-weight: 400;
    font-size: 42px;
    color: var(--sky);
    letter-spacing: 0.5px;
    white-space: nowrap;
  }
  .person { position: absolute; left: 42px; bottom: 32px; color: var(--card-white); }
  .person__name { font-family: "Tinos", serif; font-size: 36px; line-height: 1.1; white-space: nowrap; }
  .person__role { font-family: "Arimo", sans-serif; font-size: 24px; line-height: 1.2; }
  .contact-list {
    position: absolute; left: 380px; top: 244px;
    padding-left: 16px;
    border-left: 2px solid var(--card-white);
    list-style: none;
    font-family: "Arimo", sans-serif;
    font-size: 15px;
    color: var(--card-white);
  }
  .contact-list li { display: flex; align-items: center; gap: 10px; height: 28px; white-space: nowrap; }
  .contact-icon { width: 16px; height: 16px; flex: none; }
</style>
</head>
<body>

  <section class="card card-back">
    <div class="card-back__art" role="img" aria-label="Low-poly faceted pattern in light and mid blues"></div>
    <h1 class="card-back__name">Harbourline Career Partners</h1>
  </section>

  <section class="card card-front">
    <svg class="card-front__wave" viewBox="0 0 700 400" width="700" height="400" aria-hidden="true">
      <path d="M0,270 C180,270 300,230 420,180 C510,145 590,140 700,140 L700,400 L0,400 Z" fill="var(--navy)"/>
      <path d="M30,256 C200,256 300,216 420,166 C510,130 590,124 690,124" fill="none" stroke="var(--sky)" stroke-width="5" stroke-linecap="round"/>
    </svg>

    <h2 class="card-front__company">Harbourline Career Partners</h2>

    <div class="person">
      <div class="person__name">Gavin Holloway</div>
      <div class="person__role">Owner</div>
    </div>

    <ul class="contact-list">
      <li>
        <svg class="contact-icon" viewBox="0 0 16 16" aria-hidden="true"><rect width="16" height="16" rx="2" fill="#fff"/><path d="M5 3.5l2 2-1 1.2c.7 1.4 1.6 2.3 3 3l1.2-1 2 2-1.4 1.8C7.5 12 4 8.5 3.5 5z" fill="var(--navy)"/></svg>
        0481937145
      </li>
      <li>
        <svg class="contact-icon" viewBox="0 0 16 16" aria-hidden="true"><rect width="16" height="16" rx="2" fill="#fff"/><rect x="3" y="5" width="10" height="7" fill="none" stroke="var(--navy)" stroke-width="1.3"/><path d="M3 5l5 4 5-4" fill="none" stroke="var(--navy)" stroke-width="1.3"/></svg>
        gavin@hcp.com.au
      </li>
      <li>
        <svg class="contact-icon" viewBox="0 0 16 16" aria-hidden="true"><rect width="16" height="16" rx="2" fill="#fff"/><circle cx="8" cy="8" r="4.8" fill="none" stroke="var(--navy)" stroke-width="1.3"/><path d="M3.2 8h9.6M8 3.2c-2.4 2.6-2.4 7 0 9.6M8 3.2c2.4 2.6 2.4 7 0 9.6" fill="none" stroke="var(--navy)" stroke-width="1"/></svg>
        harbourlinecareer.com.au
      </li>
      <li>
        <svg class="contact-icon" viewBox="0 0 16 16" aria-hidden="true"><rect width="16" height="16" rx="2" fill="#fff"/><path d="M8 13.5s-4-4.2-4-7a4 4 0 018 0c0 2.8-4 7-4 7z" fill="var(--navy)"/><circle cx="8" cy="6.5" r="1.5" fill="#fff"/></svg>
        58 Pellimore Cres, Wardell Vic 3197
      </li>
    </ul>
  </section>

</body>
</html>
```